Verdant Medispa Business Card

need a business card for our medispa, attached please see the logo.
our website is https://verdantmedispa-example.com

Sorina Belcourt, MD
Internal Medicine

555-204-7193

Sorina@verdantmedispa-example.com

Www.Verdantmedispa-example.com

738 E Harlow Blvd N, Ste 512, Katy, TX 77981

Target Market(s)

MedSpa, Cosmetics, Esthetics

Industry/Entity Type

MedicalSpa

Contact Information for Business Card

Please see the attached business card which i pulled from the internet. I like the idea back as a logo and front with info.

Font styles to use
Decorative

Requirements
Must have
• Color should be matching with Logo and Website theme, Also I like to have QR code for the website

```html
<!DOCTYPE html>
<html lang="en">
<head>
<meta charset="utf-8">
<title>Verdant Medispa Business Card</title>
<link rel="stylesheet" href="https://fonts.googleapis.com/css2?family=Tinos:wght@400;700&display=swap">
<style>
  :root {
    --backdrop: #2a2a2e;
    --card: #231f20;
    --silver: #d9d9d9;
    --gold: #d9a72a;
    --text-light: #e6e6e6;
    --qr-light: #efefef;
  }
  * { margin: 0; padding: 0; box-sizing: border-box; }
  html, body { width: 1200px; height: 817px; overflow: hidden; }
  body {
    background: var(--backdrop);
    font-family: "Tinos", "Times New Roman", serif;
    position: relative;
  }
  .card {
    position: absolute;
    width: 540px;
    height: 310px;
    background: var(--card);
    border-radius: 22px;
    box-shadow: 0 14px 30px rgba(0,0,0,0.45);
    overflow: hidden;
  }
  .card-back { left: 50px; top: 80px; }
  .card-front { left: 610px; top: 420px; }

  .brand-name {
    font-family: "Tinos", "Times New Roman", serif;
    font-weight: 400;
    color: var(--silver);
    white-space: nowrap;
  }
  .brand-dot {
    width: 14px; height: 14px; border-radius: 50%;
    background: var(--silver);
    flex: none;
  }
  .card-back .brand {
    position: absolute;
    inset: 0;
    display: flex; align-items: center; justify-content: center; gap: 14px;
  }
  .card-back .brand-name { font-size: 40px; }

  .card-front .brand {
    position: absolute;
    left: 34px; top: 96px;
    display: flex; align-items: center; gap: 10px;
  }
  .card-front .brand-name { font-size: 26px; }
  .card-front .brand-dot { width: 10px; height: 10px; }

  .person {
    position: absolute;
    left: 34px; bottom: 34px;
  }
  .person-name {
    font-weight: 700;
    font-size: 22px;
    color: var(--gold);
    line-height: 1.1;
  }
  .person-title {
    font-size: 14px;
    color: var(--text-light);
    margin-top: 3px;
  }
  .address {
    font-style: normal;
    font-size: 14px;
    color: var(--text-light);
    margin-top: 8px;
    line-height: 1.25;
  }

  .contacts {
    position: absolute;
    right: 28px; top: 40px;
    list-style: none;
    display: flex; flex-direction: column; align-items: flex-end; gap: 10px;
  }
  .contacts li {
    display: flex; align-items: center; gap: 8px;
    font-size: 13px;
    color: var(--text-light);
    white-space: nowrap;
  }
  .contact-icon {
    width: 18px; height: 18px;
    background: var(--gold);
    border-radius: 3px;
    display: flex; align-items: center; justify-content: center;
    flex: none;
  }
  .contact-icon svg { width: 12px; height: 12px; }

  .qr-code {
    position: absolute;
    right: 28px; bottom: 30px;
    width: 80px; height: 80px;
    background: var(--qr-light);
    border-radius: 4px;
    border: 6px solid var(--qr-light);
    box-shadow: inset 0 0 0 2px var(--card);
  }
</style>
</head>
<body>

<section class="card card-back" aria-label="Card back">
  <div class="brand">
    <span class="brand-dot"></span>
    <span class="brand-name">Verdant Medispa</span>
  </div>
</section>

<section class="card card-front" aria-label="Card front">
  <div class="brand">
    <span class="brand-dot"></span>
    <span class="brand-name">Verdant Medispa</span>
  </div>

  <ul class="contacts">
    <li>
      <span>555-204-7193</span>
      <span class="contact-icon">
        <svg viewBox="0 0 24 24"><path fill="#231f20" d="M6.6 10.8a15.1 15.1 0 0 0 6.6 6.6l2.2-2.2a1 1 0 0 1 1-.25 11.4 11.4 0 0 0 3.6.57 1 1 0 0 1 1 1V20a1 1 0 0 1-1 1A17 17 0 0 1 3 4a1 1 0 0 1 1-1h3.5a1 1 0 0 1 1 1c0 1.25.2 2.45.57 3.57a1 1 0 0 1-.25 1z"/></svg>
      </span>
    </li>
    <li>
      <span>Sorina@verdantmedispa-example.com</span>
      <span class="contact-icon">
        <svg viewBox="0 0 24 24"><rect x="3" y="6" width="18" height="12" rx="1" fill="#231f20"/><path d="M3 7l9 6 9-6" fill="none" stroke="#d9a72a" stroke-width="1.6"/></svg>
      </span>
    </li>
    <li>
      <span>Www.Verdantmedispa-example.com</span>
      <span class="contact-icon">
        <svg viewBox="0 0 24 24"><path fill="#231f20" d="M5 3l14 7-6 2-2 6z"/></svg>
      </span>
    </li>
  </ul>

  <div class="qr-code" role="img" aria-label="QR code linking to https://verdantmedispa-example.com"></div>

  <div class="person">
    <p class="person-name">Sorina Belcourt, MD</p>
    <p class="person-title">Internal Medicine</p>
    <address class="address">738 E Harlow Blvd N, Ste 512,<br>Katy, TX 77981</address>
  </div>
</section>

</body>
</html>
```